Post card

I want an educational customer postcard with our logo, email, and contact number. We are a residential foundation inspection & repair company here in Los Angeles. We provide foundation repair, earthquake retrofitting, and reinforcement.
Our number is 323-555-0148.
Email info@bramblecrestworks.com
Our license number is #2839165

OUR GOAL
Our primary objective is to empower clients with comprehensive knowledge about foundation issues and earthquake retrofitting. By educating them on the potential risks associated with foundation problems and the importance of earthquake retrofitting, we aim to equip homeowners with the necessary information to make informed decisions about safeguarding their properties. Highlighting the benefits of having their houses properly bolted not only enhances structural integrity but also provides peace of mind during seismic events, ensuring the safety and security of their homes and loved ones.

```html
<!DOCTYPE html>
<html lang="en">
<head>
<meta charset="UTF-8">
<title>Bramblecrest Works – Foundation Postcard</title>
<link rel="stylesheet" href="https://fonts.googleapis.com/css2?family=Poppins:wght@300;400;500;600;700;800&family=Archivo:wght@800;900&family=Montserrat:wght@800;900&family=Open+Sans:wght@600;800&family=Yellowtail&display=swap">
<style>
  :root {
    --red: #e41e2a;
    --blue: #3b67b8;
    --ink: #141414;
    --paper: #ffffff;
    --page: #ececec;
    --rule: #9a9a9a;
  }
  * { margin: 0; padding: 0; box-sizing: border-box; }
  html, body { width: 914px; height: 1200px; overflow: hidden; }
  body { background: var(--page); position: relative; font-family: "Poppins", sans-serif; color: var(--ink); }

  .card { position: absolute; left: 110px; width: 691px; height: 466px; background: var(--paper); box-shadow: 0 2px 6px rgba(0,0,0,.18); }
  .card--front { top: 86px; }
  .card--back { top: 627px; }
  .abs { position: absolute; }

  /* brand */
  .brand { display: flex; align-items: center; gap: 8px; }
  .brand__mark { width: 30px; height: 30px; background: var(--blue); flex: none; }
  .brand__name { font-family: "Poppins", sans-serif; font-weight: 700; color: var(--blue); font-size: 21px; line-height: 1; letter-spacing: .3px; }
  .brand__license { font-size: 7px; font-weight: 600; color: var(--ink); margin-top: 4px; text-align: right; }

  /* front */
  .front-heading { left: 264px; top: 45px; font-family: "Archivo", sans-serif; font-weight: 900; font-size: 20px; line-height: 18px; letter-spacing: .3px; }
  .front-script { left: 462px; top: 30px; font-family: "Yellowtail", cursive; font-size: 54px; line-height: 1; }
  .red-panel, .front-photo, .quote-band { position: absolute; left: 0; top: 0; }
  .service-list { left: 32px; top: 122px; list-style: none; }
  .service-list li { display: flex; align-items: center; gap: 10px; color: #fff; font-size: 19px; line-height: 30.6px; font-weight: 400; }
  .service-list svg { flex: none; }
  .front-phone { left: 89px; top: 373px; width: 178px; height: 26px; background: var(--blue); color: #fff; display: flex; align-items: center; justify-content: center; gap: 6px; font-weight: 700; font-size: 20px; }
  .front-email { left: 30px; top: 401px; width: 280px; text-align: center; font-size: 15.5px; font-weight: 500; line-height: 24px; }
  .quote-text { left: 339px; top: 390px; width: 329px; text-align: center; color: #fff; font-weight: 600; font-size: 14px; line-height: 19px; }

  /* back */
  .back-photo { left: 21px; top: 28px; width: 206px; height: 204px; background: linear-gradient(160deg, #7fa3c8 0%, #c9a27a 40%, #8b3a2a 70%, #5b5048 100%); }
  .call-pill { left: 35px; top: 304px; width: 192px; height: 24px; border-radius: 12px; background: var(--blue); color: #fff; font-family: "Montserrat", sans-serif; font-weight: 800; font-size: 18px; letter-spacing: .8px; display: flex; align-items: center; justify-content: center; }
  .back-phone { left: 53px; top: 338px; display: flex; align-items: center; gap: 14px; font-weight: 600; font-size: 15px; }
  .back-rule { left: 44px; width: 182px; height: 1px; background: var(--red); }
  .back-email { left: 42px; top: 374px; font-size: 15px; font-weight: 500; }
  .back-license { left: 29px; top: 409px; font-size: 15px; font-weight: 600; }

  .why-title { left: 246px; top: 33px; font-family: "Open Sans", sans-serif; font-weight: 800; font-size: 15px; letter-spacing: .2px; }
  .why-item { display: flex; align-items: center; gap: 8px; font-family: "Open Sans", sans-serif; font-weight: 600; font-size: 11.5px; }
  .about-box { left: 228px; top: 112px; width: 439px; height: 103px; background: var(--blue); color: #fff; padding: 15px 18px 0 18px; font-size: 12.3px; font-weight: 300; line-height: 16.3px; }
  .service-band { left: 228px; top: 215px; width: 439px; height: 20px; background: var(--red); color: #fff; font-family: "Montserrat", sans-serif; font-weight: 800; font-size: 14px; letter-spacing: .45px; display: flex; align-items: center; justify-content: center; }
  .address-line { left: 274px; width: 269px; height: 1px; background: var(--rule); }
  .stamp-box { left: 564px; top: 271px; width: 103px; height: 93px; border: 1px solid var(--rule); }
</style>
</head>
<body>

<section class="card card--front">
  <div class="abs" style="left:34px;top:40px;">
    <div class="brand">
      <span class="brand__mark"></span>
      <div class="brand__name">BRAMBLECREST<br>WORKS</div>
    </div>
    <div class="brand__license">#2839165</div>
  </div>

  <h1 class="abs front-heading">FOUNDATION<br>INSPECTION &amp;<br>REPAIR</h1>
  <div class="abs front-script">Services</div>

  <svg class="red-panel" width="691" height="466" viewBox="0 0 691 466">
    <polygon points="21,112 240,112 358,383 21,383" fill="var(--red)"/>
  </svg>
  <svg class="front-photo" width="691" height="466" viewBox="0 0 691 466" role="img" aria-label="Photo of a construction crew in hard hats and safety vests reviewing plans beside a new foundation wall, with earth-moving machines and a house behind">
    <defs>
      <linearGradient id="photoTone" x1="0" y1="0" x2="0" y2="1">
        <stop offset="0" stop-color="#9fc3df"/>
        <stop offset=".35" stop-color="#d9c9a3"/>
        <stop offset=".65" stop-color="#a9a9a6"/>
        <stop offset="1" stop-color="#8a6d4a"/>
      </linearGradient>
    </defs>
    <polygon points="258,112 668,112 668,383 371,383" fill="url(#photoTone)"/>
  </svg>

  <ul class="abs service-list">
    <li><svg width="14" height="14" viewBox="0 0 14 14"><circle cx="7" cy="7" r="6.2" fill="#fff" stroke="var(--blue)" stroke-width="1.4"/><path d="M4 7.2l2 2 4-4.2" fill="none" stroke="var(--blue)" stroke-width="1.6"/></svg>House Bolting</li>
    <li><svg width="14" height="14" viewBox="0 0 14 14"><circle cx="7" cy="7" r="6.2" fill="#fff" stroke="var(--blue)" stroke-width="1.4"/><path d="M4 7.2l2 2 4-4.2" fill="none" stroke="var(--blue)" stroke-width="1.6"/></svg>Crack Repair</li>
    <li><svg width="14" height="14" viewBox="0 0 14 14"><circle cx="7" cy="7" r="6.2" fill="#fff" stroke="var(--blue)" stroke-width="1.4"/><path d="M4 7.2l2 2 4-4.2" fill="none" stroke="var(--blue)" stroke-width="1.6"/></svg>Beam Reinforcment</li>
    <li><svg width="14" height="14" viewBox="0 0 14 14"><circle cx="7" cy="7" r="6.2" fill="#fff" stroke="var(--blue)" stroke-width="1.4"/><path d="M4 7.2l2 2 4-4.2" fill="none" stroke="var(--blue)" stroke-width="1.6"/></svg>Structural Defects</li>
    <li><svg width="14" height="14" viewBox="0 0 14 14"><circle cx="7" cy="7" r="6.2" fill="#fff" stroke="var(--blue)" stroke-width="1.4"/><path d="M4 7.2l2 2 4-4.2" fill="none" stroke="var(--blue)" stroke-width="1.6"/></svg>Cripple Wall Bracing</li>
    <li><svg width="14" height="14" viewBox="0 0 14 14"><circle cx="7" cy="7" r="6.2" fill="#fff" stroke="var(--blue)" stroke-width="1.4"/><path d="M4 7.2l2 2 4-4.2" fill="none" stroke="var(--blue)" stroke-width="1.6"/></svg>Foundation Inspections</li>
    <li><svg width="14" height="14" viewBox="0 0 14 14"><circle cx="7" cy="7" r="6.2" fill="#fff" stroke="var(--blue)" stroke-width="1.4"/><path d="M4 7.2l2 2 4-4.2" fill="none" stroke="var(--blue)" stroke-width="1.6"/></svg>Foundation Crack Stitching</li>
    <li><svg width="14" height="14" viewBox="0 0 14 14"><circle cx="7" cy="7" r="6.2" fill="#fff" stroke="var(--blue)" stroke-width="1.4"/><path d="M4 7.2l2 2 4-4.2" fill="none" stroke="var(--blue)" stroke-width="1.6"/></svg>Crawl Space Encapsulation</li>
  </ul>

  <div class="abs front-phone">
    <svg width="20" height="20" viewBox="0 0 20 20"><circle cx="10" cy="10" r="9.5" fill="#fff"/><path d="M7 5.2l1.8 2.6-1.1 1.2c.7 1.5 1.8 2.6 3.3 3.3l1.2-1.1 2.6 1.8-.9 1.9c-4.2-.3-7.6-3.7-7.9-7.9z" fill="var(--blue)"/></svg>
    323-555-0148
  </div>
  <div class="abs front-email">INFO@BRAMBLECRESTWORKS.COM</div>

  <svg class="quote-band" width="691" height="466" viewBox="0 0 691 466">
    <polygon points="315,384 668,384 668,447 339,447" fill="var(--blue)"/>
  </svg>
  <p class="abs quote-text">“Your home's foundation is its backbone.<br>Trust us to keep it strong and secure!”</p>
</section>

<section class="card card--back">
  <div class="abs back-photo" role="img" aria-label="Photo of a worker in gloves tightening rebar with a wrench on a rooftop construction site above a city"></div>

  <div class="abs brand" style="left:42px;top:246px;">
    <span class="brand__mark" style="width:26px;height:26px;"></span>
    <div class="brand__name" style="font-size:19px;">BRAMBLECREST<br>WORKS</div>
  </div>

  <div class="abs call-pill">CALL US TODAY</div>
  <div class="abs back-phone">
    <svg width="22" height="22" viewBox="0 0 20 20"><circle cx="10" cy="10" r="10" fill="var(--red)"/><path d="M7 5.2l1.8 2.6-1.1 1.2c.7 1.5 1.8 2.6 3.3 3.3l1.2-1.1 2.6 1.8-.9 1.9c-4.2-.3-7.6-3.7-7.9-7.9z" fill="#fff"/></svg>
    323-555-0148
  </div>
  <div class="abs back-rule" style="top:367px;"></div>
  <div class="abs back-email">info@bramblecrestworks.com</div>
  <div class="abs back-rule" style="top:403px;"></div>
  <div class="abs back-license">license number is #2839165</div>

  <h2 class="abs why-title">WHY CHOOSE US</h2>
  <div class="abs why-item" style="left:244px;top:63px;"><svg width="11" height="10" viewBox="0 0 11 10"><path d="M1 5l3 3 6-7" fill="none" stroke="var(--ink)" stroke-width="2"/></svg>Reasonable Pricing</div>
  <div class="abs why-item" style="left:244px;top:81px;"><svg width="11" height="10" viewBox="0 0 11 10"><path d="M1 5l3 3 6-7" fill="none" stroke="var(--ink)" stroke-width="2"/></svg>Payment Plans Available</div>
  <div class="abs why-item" style="left:412px;top:63px;"><svg width="11" height="10" viewBox="0 0 11 10"><path d="M1 5l3 3 6-7" fill="none" stroke="var(--ink)" stroke-width="2"/></svg>Reasonable Pricing</div>
  <div class="abs why-item" style="left:412px;top:81px;"><svg width="11" height="10" viewBox="0 0 11 10"><path d="M1 5l3 3 6-7" fill="none" stroke="var(--ink)" stroke-width="2"/></svg>Payment Plans Available</div>

  <p class="abs about-box">BRAMBLECREST WORKS is a company born out of a passion for making California a safer place. With our expertise in the knowledge of earthquake retrofitting and our hardworking team, we have been reinforcing older homes up to current code all over California.</p>
  <div class="abs service-band">SERVICING LOS ANGELES &amp; SURROUNDING CITIES</div>

  <div class="abs address-line" style="top:296px;"></div>
  <div class="abs address-line" style="top:319px;"></div>
  <div class="abs address-line" style="top:342px;"></div>
  <div class="abs stamp-box"></div>
</section>

</body>
</html>
```